Update informational website

I need a new modern site design for my website.

Here is the site: http://q.zp/rkTm

Here is a theme I liked: http://q.zp/rkTb

I am looking for something with clean lines and an exciting designs and graphics, please use images from glentavorix.com and track the images used so I can buy them if I like the design.

I just need the homepage and one interior page designed.

Colors
Bright Green #6ed30d
Dark Text #222
Lighter Text #444

Number of Pages Required

2 page

Font styles to use
Sans Serif

Requirements
Must have
• Clean, good spacing, responsive design, high resolution design

```html
<!DOCTYPE html>
<html lang="en">
<head>
<meta charset="utf-8">
<title>About Us – Mesa Glass Tint</title>
<link href="https://fonts.googleapis.com/css2?family=Open+Sans:wght@400;600;700;800&family=Oswald:wght@400;500&display=swap" rel="stylesheet">
<style>
:root{
  --green:#6ed30d;
  --green-dark:#6a9a2a;
  --text-dark:#222;
  --text-light:#444;
  --footer-bg:#2a2a2a;
  --hero-top:#3a3a3a;
  --hero-bottom:#8a8a8a;
  --map-base:#ece8df;
  --white:#fff;
}
*{box-sizing:border-box;margin:0;padding:0}
html,body{width:772px;height:1200px;overflow:hidden;background:var(--white)}
body{position:relative;font-family:"Open Sans",Arial,sans-serif;color:var(--text-dark)}
.abs{position:absolute}

/* hero */
.hero{position:absolute;left:0;top:0;width:772px;height:252px}
.topbar-call{left:107px;top:6px;font-size:11px;font-weight:600;color:var(--white)}
.top-social{right:60px;top:7px;display:flex;gap:14px}
.top-social span{width:11px;height:11px;border-radius:50%;background:var(--white);display:block}
.brand{left:106px;top:38px;font-size:17px;font-weight:800;color:var(--green);letter-spacing:.2px}
.main-nav{top:43px;left:402px;display:flex;font-size:10.5px;font-weight:600;color:var(--white)}
.main-nav a{color:inherit;text-decoration:none;margin-right:24px}
.search{left:694px;top:41px}
.page-title{left:0;width:772px;top:116px;text-align:center;font-size:38px;font-weight:800;color:var(--white);letter-spacing:.5px}
.title-rule{left:318px;top:172px;width:136px;height:2px;background:var(--white)}

/* content */
.content{left:111px;top:287px;width:398px}
.content h2{font-size:13px;font-weight:700;color:var(--green-dark);margin-bottom:4px;letter-spacing:.2px}
.content p{font-size:7.6px;line-height:9.6px;color:var(--text-dark);margin-bottom:9px}
.content h2.store{margin-top:2px}
.content .invite{font-size:10.5px;line-height:13px;color:var(--text-light);padding-left:20px;margin-top:3px}

.sidebar{left:576px;top:287px;width:150px}
.sidebar h3{font-size:10px;font-weight:700;color:var(--green-dark);letter-spacing:.3px}
.sidebar ul{list-style:none;font-size:7.6px;line-height:16px;color:var(--text-dark);margin:2px 0 13px}
.side-social{display:flex;gap:6px;margin:12px 0 20px}
.side-social span{width:18px;height:18px;border-radius:3px;display:block}

/* map */
.map{left:0;top:598px;width:772px;height:190px}

/* footer */
.contact-band{left:0;top:798px;width:772px;height:354px;background:var(--footer-bg)}
.notch{left:365px;top:798px}
.f-head{font-family:"Oswald",Arial,sans-serif;font-size:13px;font-weight:500;color:var(--green);letter-spacing:.2px}
.f-note{font-size:7.4px;line-height:9.8px;color:var(--white)}
.field{position:absolute;left:58px;width:324px;height:27px;background:var(--white);border-radius:3px;font-size:11px;color:#999;padding:7px 10px}
.submit{left:299px;top:1102px;width:82px;height:22px;background:var(--green);color:var(--white);font-size:11.5px;text-align:center;line-height:22px;letter-spacing:.3px}
.info-label{font-size:10px;font-weight:600;color:var(--white)}
.info-value{font-size:10px;line-height:12px;color:var(--white)}
.f-follow{left:414px;top:1044px;font-size:16px;font-weight:800;color:var(--white);letter-spacing:.5px}
.f-social{left:413px;top:1078px;display:flex;gap:10px}
.f-social span{width:28px;height:28px;border-radius:4px;display:block}

.copyright{left:0;top:1167px;width:772px;text-align:center;font-size:10px;color:var(--text-light)}
</style>
</head>
<body>

<header class="hero">
  <svg class="abs" width="772" height="252" role="img" aria-label="Photo of a grey sports car parked on a night city street">
    <defs>
      <linearGradient id="heroFill" x1="0" y1="0" x2="0" y2="1">
        <stop offset="0" stop-color="#2d2d2d"/>
        <stop offset=".55" stop-color="#5c5c5c"/>
        <stop offset="1" stop-color="#3e3e3e"/>
      </linearGradient>
    </defs>
    <polygon points="0,0 772,0 772,182 388,250 0,182" fill="url(#heroFill)"/>
  </svg>
  <div class="abs topbar-call">GIVE US A CALL 555.014.2290</div>
  <div class="abs top-social" aria-hidden="true"><span></span><span></span><span></span><span></span></div>
  <div class="abs brand">Mesa Glass Tint</div>
  <nav class="abs main-nav"><a href="#">HOME</a><a href="#">ABOUT</a><a href="#">SERVICES</a><a href="#">CONTACT</a></nav>
  <svg class="abs search" width="18" height="18" viewBox="0 0 18 18" aria-label="Search"><circle cx="7.5" cy="7.5" r="6" fill="none" stroke="#fff" stroke-width="1.6"/><line x1="12" y1="12" x2="17" y2="17" stroke="#fff" stroke-width="1.8"/></svg>
  <h1 class="abs page-title">ABOUT US</h1>
  <div class="abs title-rule"></div>
</header>

<main class="abs content">
  <h2>ABOUT MESA GLASS TINT.</h2>
  <p>Mesa Glass Tint is not just another tint shop. We specialize in one thing and one thing only; Window Tinting. We offer Residential, Commercial and Automotive tinting services. Our philosophy is simple; do things right the first time! After 18 years we have learned that there is no such thing as a small job. Whether you need your personal car tinted, your new home protected or a complete face lift on your 10 story building, we believe that quality installation, attention to detail and customer service are the cornerstone's of a job well done.</p>
  <p>As a player in the Larkfield tint market for over twenty years, we have had the privilege to work with two of the best Window Film Manufacturers in the world. The knowledge and experience we have obtained in the last two decades makes us one of the most experienced operations in the valley. We know how the window film industry works, especially when it comes to factory warranties, installation guidelines and trade secrets.</p>
  <h2 class="store">OUR STORE</h2>
  <p>Mesa Glass Tint is located in the beautiful city of Larkfield Az. Our show room and oversize display boards allows automotive customers to see exactly what film and colors we have to offer. If you are looking to have your commercial building or you personal home tinted, your experience with us will be pleasant and professional. We offer in-home estimates six days a week. We offer a wide range of window films depending on your application needs. Anti-graffiti films, non-reflective films, decorative films, dual-reflective films, ceramic films and even clear window films. Let our expertise guide you in selecting the correct film for your particular needs.</p>
  <p class="invite">We are fully insured and we invite you to stop in and take a tour of our shop.</p>
</main>

<aside class="abs sidebar">
  <h3>FOLLOW US</h3>
  <div class="side-social" aria-hidden="true">
    <span style="background:#3b5998"></span><span style="background:#4aa3df"></span><span style="background:#e62117"></span><span style="background:#0077b5"></span>
  </div>
  <h3>CATEGORIES</h3>
  <ul><li>Residential Window Film</li><li>Window Film</li><li>Window Tinting</li></ul>
  <h3>ARCHIVE</h3>
  <ul><li>June 2017</li><li>May 2017</li><li>April 2017</li></ul>
</aside>

<svg class="abs map" width="772" height="190" role="img" aria-label="Street map showing the shop location">
  <rect width="772" height="190" fill="var(--map-base)"/>
</svg>

<section class="abs contact-band" role="img" aria-label="Darkened photo of a car interior behind the contact section"></section>
<svg class="abs notch" width="42" height="22" aria-hidden="true"><polygon points="0,0 42,0 21,20" fill="#fff"/></svg>

<div class="abs f-head" style="left:57px;top:838px">CONTACT US</div>
<p class="abs f-note" style="left:57px;top:863px;width:320px">Need a quote or consultation? Looking to schedule an appointment? Whatever the case may be, fill out the form below and we'll get back to you within one business day. Please give a brief description of your inquiry. Have a great day!</p>
<div class="field" style="top:904px">Name (Required)</div>
<div class="field" style="top:946px">Your Phone Number (Required)</div>
<div class="field" style="top:988px">Your Email (Required)</div>
<div class="field" style="top:1031px;height:59px">Message</div>
<div class="abs submit">SUBMIT</div>

<div class="abs f-head" style="left:410px;top:838px">PLEASE GIVE US A CALL IF YOU HAVE ANY QUESTIONS.</div>
<p class="abs f-note" style="left:410px;top:863px;width:300px">Our show room is open Monday – Friday 8:00 A.M. to 5:00 P.M.<br>and by appointment only on Saturday.<br>We try to answer all phone calls 7 days a week, 7:00 AM – 10:00 PM.</p>
<div class="abs" style="left:411px;top:902px">
  <div class="info-label">STREET ADDRESS</div>
  <div class="info-value">4120 E. Juniper Dr. Suite B<br>Larkfield, Az. 85999</div>
</div>
<div class="abs" style="left:411px;top:951px">
  <div class="info-label">TELEPHONE</div>
  <div class="info-value">555.014.2290</div>
</div>
<div class="abs" style="left:411px;top:993px">
  <div class="info-label">EMAIL</div>
  <div class="info-value">dana@mesaglasstint.com</div>
</div>
<div class="abs f-follow">FOLLOW US</div>
<div class="abs f-social" aria-hidden="true">
  <span style="background:#3b5998"></span><span style="background:#4aa3df"></span><span style="background:#e62117"></span><span style="background:#0077b5"></span>
</div>

<footer class="abs copyright">Copyright © Mesa Glass Tint, All Rights Reserved. | 4120 E. Juniper Dr. Suite B | Larkfield, Az. 85999 | 555.014.2290</footer>

</body>
</html>
```